Electrical company needs professional eye catching business cards

I am an electrician who needs business cards. I have attached two images which you can use. The file ab.jpg I would atleast like to be used. The file named back.jpg can be used on the back or not... up to you.

The information on my business cards I will have displayed will be-
My name
Mobile number
web site url
Licence number
ABN

Also as another request, I would like the word "Electrician" on the front of the card somewhere. Maybe under my name or something?

Industry/Entity Type

Electrician

```html
<!DOCTYPE html>
<html lang="en">
<head>
<meta charset="utf-8">
<title>Brightwire — Business Card</title>
<link rel="stylesheet" href="https://fonts.googleapis.com/css2?family=Open+Sans:ital,wght@0,400;0,600;0,700;1,400&display=swap">
<style>
  :root {
    --brand-blue: #213f9a;
    --card-white: #ffffff;
    --backdrop: #e6e7ea;
    --card-shadow: rgba(20, 30, 60, 0.18);
  }
  * { margin: 0; padding: 0; box-sizing: border-box; }
  html, body {
    width: 1200px;
    height: 873px;
    overflow: hidden;
    background: var(--backdrop);
    font-family: "Open Sans", Arial, sans-serif;
  }
  .canvas {
    width: 1200px;
    height: 873px;
    display: flex;
    align-items: center;
    justify-content: center;
    gap: 60px;
  }
  .card {
    position: relative;
    width: 520px;
    height: 318px;
    background: var(--brand-blue);
    box-shadow: 0 10px 28px var(--card-shadow);
    overflow: hidden;
    color: var(--card-white);
  }
  .card-front__panel {
    position: absolute;
    inset: 0;
    width: 100%;
    height: 100%;
  }
  .brand {
    font-weight: 700;
    color: var(--card-white);
    white-space: nowrap;
    line-height: 1;
  }
  .card-front .brand {
    position: absolute;
    left: 150px;
    top: 36px;
    font-size: 50px;
  }
  .contact {
    position: absolute;
    left: 150px;
    right: 20px;
    top: 104px;
    text-align: center;
    line-height: 1.15;
  }
  .contact__name { font-size: 22px; font-weight: 400; }
  .contact__role { font-size: 16px; font-style: italic; }
  .contact__mobile { font-size: 16px; }
  .contact__web { font-size: 24px; font-weight: 600; }
  .contact__licence { font-size: 24px; }
  .contact__abn { font-size: 24px; font-weight: 600; }

  .card-back {
    display: flex;
    align-items: center;
    justify-content: center;
  }
  .card-back .brand { font-size: 56px; }
</style>
</head>
<body>
  <main class="canvas">
    <section class="card card-front" aria-label="Business card front">
      <svg class="card-front__panel" viewBox="0 0 520 318" aria-hidden="true">
        <polygon points="0,0 140,0 140,100 40,318 0,318" fill="var(--card-white)"/>
      </svg>
      <p class="brand">Brightwire</p>
      <div class="contact">
        <p class="contact__name">FIRSTNAME lastname</p>
        <p class="contact__role">Electrician</p>
        <p class="contact__mobile">Mobile Number</p>
        <p class="contact__web">www.brightwire.com</p>
        <p class="contact__licence">Licence number</p>
        <p class="contact__abn">ABN</p>
      </div>
    </section>

    <section class="card card-back" aria-label="Business card back">
      <p class="brand">Brightwire</p>
    </section>
  </main>
</body>
</html>
```